new recycling company is looking for more vendors

Ridgeline Cove Recycling is a company that actively purchases surplus and obsolete equipment from various sources; hospitals, manufacturers, logistics companies... We are looking for a full page flyer that we can send to our prospective vendors to inform them about what services we provide. We would like to use the colors similar to our website here: http://marbrookrecyc.example/index.html and include the logo we have there. The attachment is just the back of an old postcard because we want to include just the list of things "we buy", not the contact info because it changed. We'd like to have the words "Reliable Convenient Secure" somewhere.

Target Market(s)

Companies with old equipment, obsolete inventories, scrap and surplus.

Industry/Entity Type

Recycling

Requirements
Must have
• I would focus more on images than text. Text should be brief, images would be great.

We want to make sure they know we buy machinery, test equipment, surplus parts and components.

Images of that type of stuff is preferred over images of computers or wire etc.

```html
<!DOCTYPE html>
<html lang="en">
<head>
<meta charset="utf-8">
<title>Ridgeline Cove Recycling – Recycle your electronics</title>
<link href="https://fonts.googleapis.com/css2?family=Lato:wght@400;700;900&family=Montserrat:wght@700&display=swap" rel="stylesheet">
<style>
  :root {
    --bg: #141414;
    --white: #ffffff;
    --grey: #9a9a9a;
    --accent: #b05a62;
    --badge: #e7dccb;
    --board-green: #2f7a58;
    --board-dark: #24493a;
    --metal: #8a8f8a;
    --metal-dark: #4a4f4b;
  }
  html, body {
    margin: 0;
    padding: 0;
    overflow: hidden;
    background: var(--bg);
  }
  .flyer {
    position: relative;
    width: 900px;
    height: 1200px;
    overflow: hidden;
    background: var(--bg);
    font-family: "Lato", Arial, sans-serif;
    color: var(--white);
  }
  .hero-photo {
    position: absolute;
    left: 0;
    top: 0;
    width: 900px;
    height: 720px;
    background:
      radial-gradient(ellipse 210px 170px at 220px 250px, rgba(47,122,88,0.95), transparent 72%),
      radial-gradient(ellipse 170px 120px at 640px 140px, rgba(138,143,138,0.7), transparent 70%),
      radial-gradient(ellipse 180px 140px at 800px 330px, rgba(36,73,58,0.85), transparent 70%),
      radial-gradient(ellipse 200px 120px at 520px 400px, rgba(47,122,88,0.55), transparent 70%),
      radial-gradient(ellipse 160px 130px at 60px 90px, rgba(138,143,138,0.6), transparent 70%),
      radial-gradient(ellipse 200px 150px at 420px 60px, rgba(74,79,75,0.9), transparent 70%),
      linear-gradient(180deg, #4f5550 0%, #3a3f3b 40%, #232523 62%, var(--bg) 92%);
  }
  .headline {
    position: absolute;
    left: 0;
    width: 900px;
    margin: 0;
    text-align: center;
    line-height: 1;
    font-weight: 900;
  }
  .headline-main {
    top: 336px;
    font-size: 222px;
    letter-spacing: -8px;
  }
  .headline-sub {
    top: 562px;
    font-size: 110px;
    letter-spacing: -4px;
  }
  .buy-list {
    position: absolute;
    left: 60px;
    top: 766px;
    margin: 0;
    padding: 0;
    list-style: none;
    font-family: "Montserrat", Arial, sans-serif;
  }
  .buy-list li {
    position: relative;
    padding-left: 27px;
    font-size: 21px;
    font-weight: 700;
    line-height: 31.6px;
  }
  .buy-list li::before {
    content: "";
    position: absolute;
    left: 0;
    top: 12px;
    border-left: 7px solid var(--white);
    border-top: 4px solid transparent;
    border-bottom: 4px solid transparent;
  }
  .brand {
    position: absolute;
    left: 607px;
    top: 752px;
    width: 186px;
    height: 186px;
    border-radius: 50%;
    background: var(--badge);
    display: flex;
    align-items: center;
    justify-content: center;
    text-align: center;
  }
  .brand-name {
    margin: 0;
    width: 140px;
    font-family: "Montserrat", Arial, sans-serif;
    font-size: 21px;
    font-weight: 700;
    line-height: 26px;
    color: var(--accent);
  }
  .contact {
    position: absolute;
    left: 522px;
    top: 983px;
    width: 340px;
    text-align: center;
    font-style: normal;
  }
  .contact-line {
    display: block;
    font-family: "Montserrat", Arial, sans-serif;
    font-size: 22px;
    font-weight: 700;
    line-height: 30px;
  }
  .contact-email {
    display: block;
    margin-top: 1px;
    font-size: 19px;
    font-weight: 400;
  }
  .copyright {
    position: absolute;
    left: 60px;
    top: 1140px;
    margin: 0;
    font-size: 16px;
    color: var(--grey);
  }
  .tagline {
    position: absolute;
    right: 48px;
    top: 1136px;
    margin: 0;
    font-family: "Montserrat", Arial, sans-serif;
    font-size: 18px;
    font-weight: 700;
    color: var(--accent);
  }
</style>
</head>
<body>
  <main class="flyer">
    <div class="hero-photo" role="img" aria-label="Heap of discarded circuit boards, machine housings and electronic equipment fading into black"></div>

    <h1 class="headline headline-main">Recycle</h1>
    <p class="headline headline-sub">your electronics</p>

    <ul class="buy-list">
      <li>Metal Fabrication Machinery</li>
      <li>Plastic Pocessing Equipment</li>
      <li>Semicondutor &amp; PCB Equipment</li>
      <li>Printing Equipment</li>
      <li>Material Handling</li>
      <li>Integrated Circuits</li>
      <li>Electronic Components</li>
      <li>Pallet Racking</li>
      <li>Test / Inspection Equipment</li>
      <li>Computers</li>
    </ul>

    <div class="brand">
      <p class="brand-name">Ridgeline Cove Recycling</p>
    </div>

    <address class="contact">
      <span class="contact-line">1480 Alder Row</span>
      <span class="contact-line">Marbrook Texas, 79912</span>
      <span class="contact-line">555.204.7731</span>
      <span class="contact-email">info@marbrookrecyc.example</span>
    </address>

    <p class="copyright">2013 © Ridgeline Cove Recycling</p>
    <p class="tagline">Reliable | Convenient | Secure</p>
  </main>
</body>
</html>
```